Our architectural studio needs a new business card

We need a business card design for our studio based in Waterloo in Belgium. We are active in architecture, design and installation.
Our works are contemporary and minimalist. our clients are refined and cultured.
Our business card must be minimalist and refined.

Project Deadline Extended
Reason: Some designers have accepted my invitation but they don't have all replied. I want to give them a chance to make one proposal. Paul

Target Market(s)

architecture

Industry/Entity Type

Business

Contact Information for Business Card

studio: paul dornevaux studio
paul dornevaux, architecte
M. +32 471 586 927
F. +322 619 4850
www.pauldornevaux-example.com
paul@pauldornevaux-example.com
14 rue des Marronniers
1420 Waterloo
Belgium

Font styles to use
Sans Serif

Requirements
Must have
• simple, minimalist, clear, elegant and chic! Black and white
Nice to have
• embossed logo, other format like a square for example
Should not have
• color, fantasy, curves, ...

```html
<!DOCTYPE html>
<html lang="en">
<head>
<meta charset="utf-8">
<title>Paul Dornevaux Studio — Business Card</title>
<link rel="stylesheet" href="https://fonts.googleapis.com/css2?family=Montserrat:wght@600&family=Open+Sans:wght@300;400&display=swap">
<style>
  :root {
    --backdrop: #c3c5c6;
    --card: #f4f4f3;
    --ink: #1a1a1a;
    --ink-soft: #4a4a4a;
    --rule: #8a8a8a;
  }
  * { margin: 0; padding: 0; box-sizing: border-box; }
  html, body {
    width: 1200px;
    height: 814px;
    overflow: hidden;
    background: var(--backdrop);
  }
  .canvas {
    width: 1200px;
    height: 814px;
    display: flex;
    align-items: center;
    justify-content: center;
    gap: 60px;
  }
  .card {
    width: 500px;
    height: 300px;
    background: var(--card);
    box-shadow: 0 18px 40px rgba(0, 0, 0, 0.18);
    position: relative;
  }

  /* Contact side */
  .card--contact {
    padding: 52px 48px 40px 62px;
    font-family: "Open Sans", sans-serif;
    font-weight: 300;
    color: var(--ink-soft);
  }
  .contact-block {
    border-left: 1px solid var(--rule);
    padding-left: 14px;
    height: 100%;
    display: flex;
    flex-direction: column;
  }
  .person-name {
    font-size: 22px;
    letter-spacing: 0.04em;
    text-transform: uppercase;
    color: var(--ink);
    line-height: 1.05;
  }
  .person-role {
    font-size: 14px;
    margin-bottom: 22px;
  }
  .details {
    display: grid;
    grid-template-columns: 1fr 1fr;
    column-gap: 24px;
    font-size: 13px;
    line-height: 1.35;
  }
  .detail { margin-bottom: 12px; }
  .detail-label {
    text-transform: uppercase;
    letter-spacing: 0.03em;
  }
  .website { margin-top: 8px; }

  /* Studio side */
  .card--studio {
    display: flex;
    flex-direction: column;
    align-items: center;
    justify-content: center;
    gap: 26px;
  }
  .studio-mark {
    width: 26px;
    height: 26px;
    background: var(--ink);
  }
  .studio-name {
    font-family: "Montserrat", sans-serif;
    font-weight: 600;
    font-size: 13px;
    letter-spacing: 0.22em;
    text-transform: uppercase;
    color: var(--ink);
  }
</style>
</head>
<body>
  <main class="canvas">
    <section class="card card--contact" aria-label="Business card, contact side">
      <div class="contact-block">
        <h1 class="person-name">Paul Dornevaux</h1>
        <p class="person-role">Architecte</p>
        <div class="details">
          <div>
            <p class="detail"><span class="detail-label">Mobile</span><br>+32 471 586 927</p>
            <p class="detail"><span class="detail-label">Fax</span><br>+322 619 4850</p>
            <p class="detail"><span class="detail-label">Email</span><br>paul@pauldornevaux-example.com</p>
          </div>
          <div>
            <p class="detail">14 rue des Marronniers<br>1420 Waterloo Belgium</p>
            <p class="website">www.pauldornevaux-example.com</p>
          </div>
        </div>
      </div>
    </section>

    <section class="card card--studio" aria-label="Business card, studio side">
      <div class="studio-mark"></div>
      <p class="studio-name">Paul Dornevaux Studio</p>
    </section>
  </main>
</body>
</html>
```